Create a website for a car broker/car buyers advocate

build a website to suit a car brokering/car buying service. The design should communicate saving people time, money and stress by outsourcing the purchasing process for thier new car. I woudl like a modern site which is scroll able all on one page and wouldnt mind a dark or minimalistic theme. i have uploaded the logo which has also been designed by pixel harbor

Target Market(s)

general consumers, new car buyers, car collectors

Industry/Entity Type

Car Dealer

Font styles to use
Sans Serif

Colors

Designer to choose colors to be used in the design.

Requirements
Must have
• single page scrollable site
• modern design
• professional but fun
Nice to have
• some websites i like of similar businesses are :
• http://www.motorvane.com.au/
• https://drivelynx.com.au/

```html
<!DOCTYPE html>
<html lang="en">
<head>
<meta charset="utf-8">
<title>Vantra Brokers</title>
<link rel="stylesheet" href="https://fonts.googleapis.com/css2?family=Lato:ital,wght@0,400;0,700;0,900;1,400&family=Open+Sans:ital,wght@0,400;0,600;0,700;1,400&display=swap">
<style>
:root{
  --navy:#3a4562;
  --sky:#7f98c8;
  --ink:#1f1f24;
  --text:#555a66;
  --muted:#6c6f78;
  --white:#ffffff;
  --footer:#1c1c21;
}
*{box-sizing:border-box;margin:0;padding:0}
html,body{width:1200px;height:4257px;overflow:hidden}
body{position:relative;background:var(--white);font-family:"Open Sans",sans-serif;color:var(--text)}
.abs{position:absolute}
.heading{font-family:"Lato",sans-serif;font-weight:700;color:var(--ink)}
.photo{position:absolute}

/* hero */
.hero{position:absolute;left:0;top:0;width:1200px;height:683px;
  background:linear-gradient(180deg,#566176 0%,#737c8e 30%,#8a8b86 42%,#6f6a5e 58%,#5a5346 100%)}
.brand{position:absolute;display:flex;align-items:center;gap:14px;font-family:"Lato",sans-serif;font-weight:700;color:var(--white);letter-spacing:5px;white-space:nowrap}
.brand-mark{width:22px;height:22px;background:var(--white);flex:none}
.hero-brand{left:109px;top:62px;font-size:24px}
.call{right:114px;top:16px;color:var(--white);font-size:17px;font-weight:600;display:flex;align-items:center;gap:8px}
.nav{left:429px;top:70px;display:flex;gap:23px;font-size:14.5px;font-weight:600;color:var(--white);text-transform:uppercase}
.save{left:977px;top:58px;width:109px;height:43px;border:2px solid var(--white);border-radius:22px;color:var(--white);font-size:14px;font-weight:700;display:flex;align-items:center;justify-content:center}
.hero-title{left:0;width:1200px;top:172px;text-align:center;font-family:"Lato",sans-serif;font-weight:700;font-size:48px;color:var(--white);letter-spacing:.5px}
.select{top:269px;width:240px;height:47px;background:var(--white);font-size:15px;color:#666;display:flex;align-items:center;justify-content:space-between;padding:0 18px}
.select::after{content:"";border:6px solid transparent;border-top:7px solid #555;margin-top:6px}
.go{left:902px;top:264px;width:153px;height:57px;background:#161618;border-radius:29px;color:var(--white);font-size:16px;font-weight:700;display:flex;align-items:center;justify-content:center}
.slide-arrow{top:316px;width:34px;height:48px;background:rgba(40,44,56,.75)}

/* welcome */
.kicker{left:112px;top:778px;font-size:33px;font-weight:400;color:var(--ink)}
.welcome-name{left:112px;top:818px;font-size:50px}
.welcome-copy{left:112px;top:906px;width:462px;font-size:14.5px;line-height:30px;color:var(--text)}
.btn-dark{left:112px;top:1094px;width:143px;height:50px;border-radius:25px;background:var(--navy);color:var(--white);font-size:15px;font-weight:700;display:flex;align-items:center;justify-content:center}
.video{left:612px;top:803px;width:476px;height:331px;background:linear-gradient(135deg,#d9dde2 0%,#a9afb6 45%,#6f747c 100%)}
.play{left:820px;top:940px;width:58px;height:58px;border-radius:50%;background:rgba(30,30,30,.8)}
.play::after{content:"";position:absolute;left:23px;top:17px;border-left:19px solid var(--white);border-top:12px solid transparent;border-bottom:12px solid transparent}

/* choose */
.choose{position:absolute;left:0;top:1261px;width:1200px;height:595px}
.choose-title{left:0;width:1200px;top:1330px;text-align:center;font-size:50px;color:var(--white)}
.choose-car{top:1432px;width:420px;height:260px}
.btn-ghost{height:53px;width:143px;border:2px solid var(--white);border-radius:27px;color:var(--white);font-size:16px;font-weight:700;display:flex;align-items:center;justify-content:center}

/* services */
.section-title{left:0;width:1200px;text-align:center;font-size:54px}
.service-img{top:2074px;width:306px;height:235px}
.service-name{top:2343px;font-size:27px;font-weight:400;color:#222}
.service-copy{top:2394px;width:310px;font-size:13.5px;line-height:29px;color:var(--muted)}
.btn-line{top:2509px;width:142px;height:50px;border:2px solid var(--navy);border-radius:25px;color:var(--navy);font-size:15px;font-weight:700;display:flex;align-items:center;justify-content:center}

/* testimonials */
.testimonials{left:0;top:2671px;width:1200px;height:519px;background:linear-gradient(90deg,#3e3f45 0%,#55575d 45%,#4a4b50 100%)}
.test-car{left:630px;top:2671px;width:570px;height:519px;background:linear-gradient(160deg,#6a6b70 0%,#8c1c22 45%,#5a1216 80%,#3f4045 100%)}
.test-title{left:111px;top:2755px;font-size:54px;color:var(--white)}
.quote{left:111px;top:2853px;width:520px;font-family:"Lato",sans-serif;font-style:italic;font-size:19px;line-height:34px;color:#e6e7ea}
.author{left:111px;top:3068px;font-size:19px;font-weight:700;color:var(--white)}
.dot-arrow{top:3072px;width:20px;height:20px;border-radius:50%;background:var(--white)}

/* cars */
.car-card{top:3398px;width:233px;height:250px;border:1px solid #cfd1d6}
.car-img{position:absolute;left:0;top:0;width:100%;height:195px}
.car-name{position:absolute;left:0;right:0;top:207px;text-align:center;font-size:20px;font-weight:600;color:var(--ink)}
.round{top:3499px;width:46px;height:46px;border:1.5px solid #777;border-radius:50%}

/* footer */
.footer{left:0;top:3749px;width:1200px;height:508px;background:var(--footer)}
.footer-brand{left:0;width:1200px;justify-content:center;top:3920px;font-size:36px;letter-spacing:9px}
.foot-line{left:0;width:1200px;text-align:center;color:#d7d8dc;font-size:14px}
.foot-line span{margin:0 10px}
.social{top:4157px;width:46px;height:46px;border:1.5px solid var(--white);border-radius:50%}
</style>
</head>
<body>

<!-- hero -->
<header class="hero" role="img" aria-label="Silver compact SUV parked on a gravel plain with snowy mountains behind">
  <div class="brand hero-brand"><span class="brand-mark"></span>VANTRA BROKERS</div>
  <div class="abs call">
    <svg width="16" height="16" viewBox="0 0 24 24"><path fill="#fff" d="M6.6 10.8a15 15 0 0 0 6.6 6.6l2.2-2.2c.3-.3.7-.4 1-.2 1.1.4 2.3.6 3.6.6.6 0 1 .4 1 1V20c0 .6-.4 1-1 1A17 17 0 0 1 3 4c0-.6.4-1 1-1h3.5c.6 0 1 .4 1 1 0 1.3.2 2.5.6 3.6.1.3 0 .7-.2 1z"/></svg>
    Call us: 1 800 555 0142
  </div>
  <nav class="abs nav"><span>About</span><span>Services</span><span>Our Stock</span><span>Research</span><span>Finance</span><span>Blog</span></nav>
  <div class="abs save">SAVE NOW</div>
  <h1 class="abs hero-title">SAVING PEOPLE TIME, MONEY &amp; STRESS</h1>
  <div class="abs select" style="left:144px">New/Used</div>
  <div class="abs select" style="left:397px">Select the make</div>
  <div class="abs select" style="left:650px">Select the model</div>
  <div class="abs go">GET STARTED</div>
  <svg class="abs slide-arrow" style="left:0" viewBox="0 0 34 48"><path d="M21 15l-9 9 9 9" stroke="#fff" stroke-width="3" fill="none"/></svg>
  <svg class="abs slide-arrow" style="left:1166px" viewBox="0 0 34 48"><path d="M13 15l9 9-9 9" stroke="#fff" stroke-width="3" fill="none"/></svg>
</header>

<!-- welcome -->
<h2 class="abs kicker heading" style="font-weight:400">WELCOME TO</h2>
<h2 class="abs welcome-name heading">VANTRA BROKERS</h2>
<p class="abs welcome-copy">Nam libero tempore, cum soluta nobis est eligendi optio cumque nihil impedit quo minus id quod maxime placeat facere possimus, omnis voluptas assumenda est, omnis dolor repellendus ribus aut em quibusdam et aut officiis debitis aut rerum necessitatibus sae pe eveniet ut et voluptates repudia.</p>
<div class="abs btn-dark">READ MORE</div>
<div class="photo video" role="img" aria-label="Video still of a broker shaking hands with a client in a car showroom"></div>
<div class="abs play"></div>

<!-- choose -->
<svg class="choose" viewBox="0 0 1200 595" preserveAspectRatio="none">
  <rect width="1200" height="595" fill="#7f98c8"/>
  <polygon points="0,0 542,0 652,595 0,595" fill="#3a4562"/>
  <polygon points="542,0 550,0 662,595 652,595" fill="#fff"/>
</svg>
<div class="photo choose-car" style="left:158px;background:linear-gradient(160deg,#c2b8a2,#8a826f)" role="img" aria-label="Weathered used SUV, front three-quarter view"></div>
<div class="photo choose-car" style="left:606px;background:linear-gradient(160deg,#e4e6e9,#a4a9b0)" role="img" aria-label="New silver SUV, front three-quarter view"></div>
<h2 class="abs choose-title heading" style="color:#fff">KNOW WHAT YOU WANT?</h2>
<div class="abs btn-ghost" style="left:245px;top:1736px">USED CAR</div>
<div class="abs btn-ghost" style="left:812px;top:1736px">NEW CAR</div>

<!-- services -->
<h2 class="abs section-title heading" style="top:1956px">MY SERVICE EXPLAINED</h2>
<div class="photo service-img" style="left:111px;background:linear-gradient(135deg,#e4e6e9,#b6bac0)" role="img" aria-label="Smiling broker holding a folder in a showroom"></div>
<div class="photo service-img" style="left:446px;background:linear-gradient(135deg,#d7d9dc,#8d97a8)" role="img" aria-label="Two men discussing paperwork at a dealership table"></div>
<div class="photo service-img" style="left:782px;background:linear-gradient(135deg,#b9bcc2,#5b5150)" role="img" aria-label="Couple looking at a new car in a showroom"></div>
<h3 class="abs service-name heading" style="left:111px">We Can Help You!</h3>
<h3 class="abs service-name heading" style="left:446px">Dealer Tricks</h3>
<h3 class="abs service-name heading" style="left:782px">New Way Of Buying</h3>
<p class="abs service-copy" style="left:111px">Nam libero tempore, cum soluta nobis est el igendi optio cumque nihil impedit quo minus id quod maxime placeat fac.</p>
<p class="abs service-copy" style="left:446px">Nam libero tempore, cum soluta nobis est el igendi optio cumque nihil impedit quo minus id quod maxime placeat fac.</p>
<p class="abs service-copy" style="left:782px">Nam libero tempore, cum soluta nobis est el igendi optio cumque nihil impedit quo minus id quod maxime placeat fac.</p>
<div class="abs btn-line" style="left:112px">READ MORE</div>
<div class="abs btn-line" style="left:448px">READ MORE</div>
<div class="abs btn-line" style="left:784px">READ MORE</div>

<!-- testimonials -->
<section class="abs testimonials"></section>
<div class="photo test-car" role="img" aria-label="Red sports coupe on a road under a stormy sky"></div>
<h2 class="abs test-title heading" style="color:#fff">TESTIMONIALS</h2>
<p class="abs quote">Nemo enim ipsam voluptatem quia voluptas sit aspernatur aut odit aut fugit, sed quia consequuntur magni dolores eos qui rat ione voluptatem sequi nesciunt. Neque porro quisquam estqui dolorem ipsum quia dolor sit amet, consectetur, adipisci velit, sed quia non numquam eius modi te.</p>
<div class="abs author">- MARK ELLISON</div>
<svg class="abs dot-arrow" style="left:544px" viewBox="0 0 20 20"><path d="M12 5l-5 5 5 5" stroke="#444" stroke-width="2.5" fill="none"/></svg>
<svg class="abs dot-arrow" style="left:569px" viewBox="0 0 20 20"><path d="M8 5l5 5-5 5" stroke="#444" stroke-width="2.5" fill="none"/></svg>

<!-- best cars -->
<h2 class="abs section-title heading" style="top:3286px">BEST CARS</h2>
<svg class="abs round" style="left:32px" viewBox="0 0 46 46"><path d="M26 15l-8 8 8 8" stroke="#555" stroke-width="2" fill="none"/></svg>
<svg class="abs round" style="left:1121px" viewBox="0 0 46 46"><path d="M20 15l8 8-8 8" stroke="#555" stroke-width="2" fill="none"/></svg>
<div class="abs car-card" style="left:111px"><div class="car-img" style="background:linear-gradient(160deg,#d0d3d7,#6e7278)" role="img" aria-label="Black hatchback driving on an open road"></div><div class="car-name">Finibus Bonet Malo</div></div>
<div class="abs car-card" style="left:359px"><div class="car-img" style="background:linear-gradient(170deg,#86a8c8,#5b7a48)" role="img" aria-label="Dark sedan on a country road with green hills"></div><div class="car-name">Finibus Bonet Malo</div></div>
<div class="abs car-card" style="left:608px"><div class="car-img" style="background:linear-gradient(170deg,#7f8fa6,#3c4660)" role="img" aria-label="Blue station wagon in front of mountains"></div><div class="car-name">Finibus Bonet Malo</div></div>
<div class="abs car-card" style="left:855px"><div class="car-img" style="background:linear-gradient(150deg,#d8b98e,#3d4a58)" role="img" aria-label="Matte grey coupe at sunset"></div><div class="car-name">Finibus Bonet Malo</div></div>

<!-- footer -->
<footer class="abs footer"></footer>
<div class="brand footer-brand"><span class="brand-mark" style="width:30px;height:30px"></span>VANTRA BROKERS</div>
<div class="abs foot-line" style="top:4018px">
  <svg width="11" height="13" viewBox="0 0 24 30"><path fill="#fff" d="M12 0a10 10 0 0 0-10 10c0 8 10 20 10 20s10-12 10-20A10 10 0 0 0 12 0zm0 14a4 4 0 1 1 0-8 4 4 0 0 1 0 8z"/></svg>
  418 Fenwick Lane, Dorset City, Maryland, Usa<span>|</span><svg width="12" height="12" viewBox="0 0 24 24"><path fill="#fff" d="M6.6 10.8a15 15 0 0 0 6.6 6.6l2.2-2.2c.3-.3.7-.4 1-.2 1.1.4 2.3.6 3.6.6.6 0 1 .4 1 1V20c0 .6-.4 1-1 1A17 17 0 0 1 3 4c0-.6.4-1 1-1h3.5c.6 0 1 .4 1 1 0 1.3.2 2.5.6 3.6.1.3 0 .7-.2 1z"/></svg> 1 800 555 0142<span>|</span><svg width="14" height="11" viewBox="0 0 24 18"><rect width="24" height="18" rx="2" fill="#fff"/><path d="M1 2l11 8 11-8" stroke="#1c1c21" stroke-width="2" fill="none"/></svg> info@vantrabrokers.com
</div>
<div class="abs foot-line" style="top:4058px">Help<span>|</span>FAQ<span>|</span>Support<span>|</span>Sitemap<span>|</span>Terms &amp; Conditions<span>|</span>Privacy Statement</div>
<div class="abs foot-line" style="top:4096px">Vantra Brokers © 2019 All rights reserved.</div>
<div class="abs social" style="left:489px" aria-label="Social link"></div>
<div class="abs social" style="left:547px" aria-label="Social link"></div>
<div class="abs social" style="left:607px" aria-label="Social link"></div>
<div class="abs social" style="left:665px" aria-label="Social link"></div>

</body>
</html>
```